Wordpress Web Design For Midlifers.com

We're looking to update the design for www.midlifers.com. The website provides news and views for people aged 50 plus.

We want to use Wordpress as the content management tool and incorporate mailchimp to manage subscribers to our monthly newsletter.

In terms of design, we're looking for something simple and straightforward, we quite like the elder hub site, so something like that would be good. http://www.elderhub.org.uk
Updates

Project Deadline Extended
Reason: Dear All, Due to the Xmas break in the UK I've decided to extend the deadline by 7 days. Thanks for all your submissions, we will be making a decision shortly. Please note, as per the original brief, we are only interested in fully coded sites uploaded to our hosting provider. Please withdraw your design if you are not able to offer this complete solution. Thanks and good wishes to all!

Requirements
Must have
• Fully working wordpress templates that allow us to easily manage the website content. Easy for readers to use, navigate and read the content.
• Ideally a'turnkey' solution - the website built and ready for us to use wordpress to populate with content.

```html
<!DOCTYPE html>
<html lang="en">
<head>
<meta charset="utf-8">
<title>Midlifers.com – News and views for people aged 50 plus</title>
<link rel="stylesheet" href="https://fonts.googleapis.com/css2?family=Open+Sans:wght@400;600;700&family=Arimo:wght@400;700&display=swap">
<style>
  :root {
    --green: #8cc63f;
    --green-dark: #7a9a1e;
    --red: #e5332a;
    --ink: #333333;
    --muted: #8a8a8a;
    --bar: #f7f7f7;
    --line: #e4e4e4;
    --ad: #2a2a2a;
    --white: #ffffff;
    --overlay: rgba(0,0,0,0.55);
  }
  * { box-sizing: border-box; margin: 0; padding: 0; }
  html, body { width: 1200px; height: 800px; overflow: hidden; }
  body { position: relative; background: var(--white); font-family: "Open Sans", sans-serif; color: var(--ink); }
  .abs { position: absolute; white-space: nowrap; }

  /* top bar */
  .topbar { left: 0; top: 0; width: 1200px; height: 43px; background: var(--bar); border-top: 3px solid var(--green); border-bottom: 1px solid var(--line); }
  .topbar__date { left: 128px; top: 13px; font-size: 12px; color: var(--muted); }
  .topbar__link { top: 12px; font-size: 13px; color: var(--muted); }
  .search { left: 659px; top: 8px; width: 174px; height: 30px; background: var(--white); border: 1px solid var(--line); font-size: 12px; color: #999; padding: 7px 7px; }
  .social { top: 8px; width: 29px; height: 29px; border-radius: 2px; }

  /* header */
  .brand { left: 140px; top: 100px; display: flex; align-items: center; gap: 12px; }
  .brand__dot { width: 40px; height: 40px; border-radius: 50%; background: var(--green); }
  .brand__name { font-size: 30px; font-weight: 600; color: #4a4a4a; }
  .ad-slot { left: 603px; top: 85px; width: 469px; height: 63px; background: var(--ad); }

  /* nav */
  .nav__item { top: 180px; height: 33px; line-height: 33px; font-size: 14px; color: #333; }
  .nav__item--active { left: 128px; width: 66px; background: var(--green); color: var(--white); text-align: center; }
  .cart { left: 900px; top: 186px; }

  /* breaking news */
  .ticker { left: 128px; top: 218px; width: 849px; height: 34px; background: #f2f2f2; }
  .ticker__label { left: 0; top: 0; width: 117px; height: 34px; background: var(--red); color: var(--white); font-size: 12px; font-weight: 700; line-height: 34px; text-align: center; }
  .ticker__text { left: 137px; top: 8px; font-size: 14px; color: #666; }

  /* hot news */
  .section-tab { left: 128px; top: 308px; width: 119px; height: 41px; background: #f5f5f5; font-size: 18px; font-weight: 700; color: #333; line-height: 41px; text-align: center; }
  .section-rule { left: 128px; top: 349px; width: 940px; height: 3px; background: var(--green-dark); }
  .section-rule__under { left: 128px; top: 349px; width: 119px; height: 3px; background: #333; }
  .pager { width: 28px; height: 28px; background: #f0f0f0; display: flex; align-items: center; justify-content: center; }
  .pager--dark { background: #1c1c1c; }

  .card { top: 362px; width: 226px; height: 157px; overflow: hidden; }
  .card__label { position: absolute; left: 0; bottom: 0; background: var(--overlay); color: var(--white); font-family: "Arimo", sans-serif; font-weight: 700; font-size: 14px; letter-spacing: -0.4px; padding: 9px 10px; white-space: nowrap; }
  .card--toys { left: 129px; background: linear-gradient(135deg, #c9a486, #d8cfc3 55%, #8e8a7e); }
  .card--alley { left: 366px; background: linear-gradient(160deg, #2c2a1c, #6a5232 55%, #1e1d14); }
  .card--city { left: 603px; background: linear-gradient(180deg, #c9cbcd, #9da1a4 60%, #55575a); }
  .card--desk { left: 840px; background: linear-gradient(135deg, #d6e5f0, #e9e4dc 50%, #c9a27a); }

  /* feature */
  .feature { left: 129px; top: 548px; width: 610px; height: 252px; background: linear-gradient(170deg, #b8c7cf 0%, #d8b99a 35%, #b86d45 65%, #7d6a5c 100%); }
  .feature__tag { left: 129px; top: 548px; width: 60px; height: 36px; background: var(--green-dark); color: var(--white); font-size: 13px; font-weight: 600; line-height: 36px; text-align: center; }
  .dot { top: 558px; width: 11px; height: 11px; border-radius: 50%; background: rgba(60,40,30,0.55); }
  .dot--on { background: var(--white); }

  .side-card { left: 773px; top: 548px; width: 295px; height: 212px; background: linear-gradient(160deg, #2b2a1c, #6b5533 55%, #1d1c13); }
  .side-card__label { left: 773px; top: 724px; background: var(--overlay); color: var(--white); font-family: "Arimo", sans-serif; font-size: 14px; letter-spacing: -0.2px; padding: 9px 10px; }
  .side-stub { left: 773px; top: 785px; width: 113px; height: 15px; background: #f3f3f3; }
</style>
</head>
<body>
  <header>
    <div class="abs topbar"></div>
    <span class="abs topbar__date">Wednesday , 18 December 2013</span>
    <span class="abs topbar__link" style="left:328px">Short Codes</span>
    <span class="abs topbar__link" style="left:420px">Forums</span>
    <div class="abs search">Search ...</div>
    <span class="abs social" style="left:846px;background:#3b5998" aria-label="Social link"></span>
    <span class="abs social" style="left:879px;background:#2fa9e0" aria-label="Social link"></span>
    <span class="abs social" style="left:912px;background:#f39a1e" aria-label="Feed link"></span>
    <span class="abs social" style="left:945px;background:#d9432f" aria-label="Social link"></span>
    <span class="abs social" style="left:978px;background:#e67ab0" aria-label="Social link"></span>
    <span class="abs social" style="left:1011px;background:#86cfe0" aria-label="Social link"></span>
    <span class="abs social" style="left:1041px;background:#f26a2e" aria-label="Social link"></span>

    <div class="abs brand">
      <span class="brand__dot"></span>
      <span class="brand__name">Midlifers.com</span>
    </div>
    <div class="abs ad-slot" role="img" aria-label="Advertising banner space"></div>

    <nav>
      <span class="abs nav__item nav__item--active">Home</span>
      <span class="abs nav__item" style="left:206px">Categories</span>
      <span class="abs nav__item" style="left:302px">Post Formats</span>
      <span class="abs nav__item" style="left:414px">Post Layout</span>
      <span class="abs nav__item" style="left:517px">Post Reviews</span>
      <span class="abs nav__item" style="left:628px">Page Templates</span>
      <span class="abs nav__item" style="left:757px">Portfolio</span>
      <span class="abs nav__item" style="left:840px">Shop</span>
    </nav>
    <svg class="abs cart" width="18" height="16" viewBox="0 0 18 16" aria-label="Cart">
      <path d="M0 1h3l2.5 9h9L17 4H5" fill="none" stroke="#333" stroke-width="2"/>
      <path d="M5 4h12l-2.5 6h-9z" fill="#333"/>
      <circle cx="7" cy="14" r="1.6" fill="#333"/><circle cx="14" cy="14" r="1.6" fill="#333"/>
    </svg>

    <div class="abs ticker">
      <div class="abs ticker__label">BREAKING NEWS</div>
      <div class="abs ticker__text">Morbi non nibh sit</div>
    </div>
  </header>

  <main>
    <div class="abs section-tab">Hot News</div>
    <div class="abs section-rule"></div>
    <div class="abs section-rule__under"></div>
    <div class="abs pager" style="left:1005px;top:320px"><svg width="8" height="12" viewBox="0 0 8 12"><path d="M6 1 1 6l5 5" fill="none" stroke="#c8c8c8" stroke-width="2"/></svg></div>
    <div class="abs pager" style="left:1039px;top:320px"><svg width="8" height="12" viewBox="0 0 8 12"><path d="M2 1l5 5-5 5" fill="none" stroke="#c8c8c8" stroke-width="2"/></svg></div>

    <article class="abs card card--toys" role="img" aria-label="Photo of collectible toys on a desk"><span class="card__label">Blog Sound Cloud Post</span></article>
    <article class="abs card card--alley" role="img" aria-label="Photo of an old stone street at night"><span class="card__label">Blog Image Post</span></article>
    <article class="abs card card--city" role="img" aria-label="Photo of a city skyline seen from a rooftop"><span class="card__label">Ut porttitor euismod</span></article>
    <article class="abs card card--desk" role="img" aria-label="Photo of a desk with a keyboard and papers"><span class="card__label">Curabitur malesuada</span></article>

    <div class="abs feature" role="img" aria-label="Photo of a canal lined with colourful buildings"></div>
    <div class="abs feature__tag">videos</div>
    <span class="abs dot" style="left:663px"></span>
    <span class="abs dot dot--on" style="left:690px"></span>
    <span class="abs dot" style="left:705px"></span>
    <span class="abs dot" style="left:719px"></span>

    <div class="abs side-card" role="img" aria-label="Photo of an old stone street at night"></div>
    <div class="abs pager pager--dark" style="left:997px;top:559px"><svg width="8" height="12" viewBox="0 0 8 12"><path d="M6 1 1 6l5 5" fill="none" stroke="#fff" stroke-width="2"/></svg></div>
    <div class="abs pager pager--dark" style="left:1030px;top:559px"><svg width="8" height="12" viewBox="0 0 8 12"><path d="M2 1l5 5-5 5" fill="none" stroke="#fff" stroke-width="2"/></svg></div>
    <div class="abs side-card__label">Blog Image Post</div>
    <div class="abs side-stub"></div>
  </main>
</body>
</html>
```